Boutique Wealth management firm needs a new business card design

I want to update my business card design to be more consistent with the look and feel of my website (www.brisvane-wealth.com). I would like to incorporate an ivory parchment background and am open to switching from the current "portrait" layout to a more traditional "landscape" orientation. The final design should convey stability and exclusivity and I want something in PDF format that is ready to send to the printer

Thank you all for taking the time to submit your designs for my project. I've made my decision and picked the design I like best. Thanks again!

```html
<!DOCTYPE html>
<html lang="en">
<head>
<meta charset="utf-8">
<title>Brisvane Wealth Advisory – Business Card</title>
<link rel="stylesheet" href="https://fonts.googleapis.com/css2?family=Open+Sans:wght@400;600;700&family=Roboto:wght@500;700&display=swap">
<style>
  :root {
    --backdrop: #2a1416;
    --parchment-light: #fbf3d6;
    --parchment-mid: #f1e2b2;
    --parchment-edge: #e6d199;
    --plum: #6b2440;
    --ink: #1c1412;
    --band-text: #f6ecd0;
  }
  * { margin: 0; padding: 0; box-sizing: border-box; }
  html, body {
    width: 1200px; height: 800px; overflow: hidden;
    background: var(--backdrop);
  }
  .canvas {
    width: 1200px; height: 800px;
    display: flex; align-items: center; justify-content: center;
  }
  .card {
    position: relative;
    width: 900px; height: 514px;
    background:
      radial-gradient(ellipse at 30% 40%, var(--parchment-light) 0%, transparent 60%),
      radial-gradient(ellipse at 75% 70%, var(--parchment-light) 0%, transparent 55%),
      radial-gradient(ellipse at 50% 50%, var(--parchment-mid) 30%, var(--parchment-edge) 100%);
    box-shadow: 0 12px 40px rgba(0,0,0,0.5);
    font-family: "Open Sans", sans-serif;
    color: var(--ink);
  }
  .holder {
    position: absolute; top: 34px; right: 48px; text-align: right;
    font-family: "Roboto", sans-serif;
  }
  .holder-name { font-size: 26px; font-weight: 700; color: var(--plum); }
  .holder-name sup { font-size: 13px; }
  .holder-title { font-size: 15px; font-weight: 700; color: var(--ink); margin-top: -2px; }
  .firm-name {
    position: absolute; left: 62px; top: 104px;
    font-family: "Open Sans", sans-serif;
    font-weight: 700; color: var(--plum);
    font-size: 44px; line-height: 1.05;
  }
  .tagline-band {
    position: absolute; left: 0; right: 0; top: 226px; height: 26px;
    background: var(--plum);
    display: flex; align-items: center;
    padding-left: 38px;
    color: var(--band-text);
    font-size: 15px; letter-spacing: 1.05em;
    white-space: nowrap; overflow: hidden;
  }
  .contact-list {
    position: absolute; left: 50px; top: 272px;
    list-style: none; font-size: 23px; line-height: 1.28;
  }
  .contact-list li { display: flex; align-items: flex-start; gap: 10px; }
  .contact-list li.address { margin-top: 12px; }
  .contact-icon { width: 22px; height: 22px; margin-top: 6px; flex-shrink: 0; fill: var(--plum); }
  .license { position: absolute; left: 86px; top: 448px; font-size: 23px; }
</style>
</head>
<body>
<main class="canvas">
  <article class="card">
    <div class="holder">
      <div class="holder-name">Dale Morven, CFP<sup>®</sup></div>
      <div class="holder-title">Principal</div>
    </div>

    <div class="firm-name">Brisvane<br>Wealth Advisory</div>

    <div class="tagline-band">GUIDING YOUR FUTURE WITH CARE</div>

    <ul class="contact-list">
      <li>
        <svg class="contact-icon" viewBox="0 0 24 24" aria-hidden="true"><path d="M6.6 10.8a15 15 0 0 0 6.6 6.6l2.2-2.2c.3-.3.7-.4 1-.2 1.1.4 2.3.6 3.6.6.6 0 1 .4 1 1V20c0 .6-.4 1-1 1A17 17 0 0 1 3 4c0-.6.4-1 1-1h3.5c.6 0 1 .4 1 1 0 1.3.2 2.5.6 3.6.1.3 0 .7-.2 1z"/></svg>
        <span>555-014-2870</span>
      </li>
      <li>
        <svg class="contact-icon" viewBox="0 0 24 24" aria-hidden="true"><path d="M2 5h20v14H2z M4 7v.4l8 5.2 8-5.2V7z" fill-rule="evenodd"/></svg>
        <span>dale@brisvane-wealth.com</span>
      </li>
      <li>
        <svg class="contact-icon" viewBox="0 0 24 24" aria-hidden="true"><circle cx="12" cy="12" r="10"/><g fill="none" stroke="#f6ecd0" stroke-width="1.4"><ellipse cx="12" cy="12" rx="4" ry="10"/><path d="M2 12h20M4 7h16M4 17h16"/></g></svg>
        <span>www.brisvane-wealth.com</span>
      </li>
      <li class="address">
        <svg class="contact-icon" viewBox="0 0 24 24" aria-hidden="true"><path d="M12 3l10 9h-3v9h-5v-6h-4v6H5v-9H2z"/></svg>
        <span>212 N. Alder Rd. #104<br>Larkfield, CA 94000</span>
      </li>
    </ul>

    <div class="license">CA Insurance License #0K58213</div>
  </article>
</main>
</body>
</html>
```